Business Card Design

We develop / design / build affordable housing throughout the state of Illinois.

Target Market(s)

non profit organizations and other developers / professionals in my industry

Industry/Entity Type

Business

Contact Information for Business Card

Verdell Ridge Construction, LLC
General Contracting
Marisol K Thornbury, CEO
418 North Wendell P Ashcroft Avenue, Suite 307
Brantwell, IL 60199
630-555-0148
mkt@buildverdellridge.com

```html
<!DOCTYPE html>
<html lang="en">
<head>
<meta charset="utf-8">
<title>Verdell Ridge Construction – Business Card</title>
<link href="https://fonts.googleapis.com/css2?family=Open+Sans:wght@400;700&display=swap" rel="stylesheet">
<style>
  :root {
    --backdrop: #d7e0df;
    --card-dark: #271f20;
    --card-light: #ffffff;
    --ink: #1f1a1b;
    --ink-reverse: #ffffff;
  }
  * { margin: 0; padding: 0; box-sizing: border-box; }
  html, body {
    width: 1200px;
    height: 1000px;
    overflow: hidden;
    background: var(--backdrop);
    font-family: "Open Sans", sans-serif;
  }
  .canvas { position: relative; width: 1200px; height: 1000px; }

  .card { position: absolute; top: 348px; height: 322px; overflow: hidden; }
  .card-front { left: 40px; width: 551px; background: var(--card-dark); }
  .card-back { left: 610px; width: 550px; background: var(--card-light); color: var(--ink); }

  .brand-mark {
    position: absolute;
    display: flex;
    align-items: center;
    font-weight: 700;
    white-space: nowrap;
  }
  .brand-mark .brand-square { display: block; flex: none; }

  .card-front .brand-mark {
    left: 43px;
    bottom: 43px;
    color: var(--ink-reverse);
    font-size: 20px;
    gap: 10px;
  }
  .card-front .brand-square { width: 16px; height: 16px; background: var(--ink-reverse); }

  .card-back .brand-mark {
    left: 47px;
    top: 89px;
    color: var(--ink);
    font-size: 11px;
    gap: 5px;
  }
  .card-back .brand-square { width: 9px; height: 9px; background: var(--ink); }

  .holder-name {
    position: absolute;
    left: 163px;
    top: 82px;
    font-size: 23px;
    font-weight: 700;
    letter-spacing: -0.4px;
    white-space: nowrap;
  }

  .contact {
    position: absolute;
    left: 47px;
    top: 166px;
    font-size: 13.5px;
    line-height: 18.5px;
    white-space: nowrap;
  }
  .contact .company { font-weight: 700; margin-top: 10px; }
</style>
</head>
<body>
<div class="canvas">
  <section class="card card-front">
    <div class="brand-mark"><span class="brand-square"></span>Verdell Ridge</div>
  </section>

  <section class="card card-back">
    <div class="brand-mark"><span class="brand-square"></span>Verdell Ridge</div>
    <h1 class="holder-name">Marisol K. Thornbury, CEO</h1>
    <div class="contact">
      <p>630-555-0148</p>
      <p>mkt@buildverdellridge.com</p>
      <p class="company">Verdell Ridge Construction, LLC</p>
      <p>General Contracting</p>
      <p>418 North Wendell P Ashcroft Avenue, Suite 307</p>
      <p>Brantwell, IL 60199</p>
    </div>
  </section>
</div>
</body>
</html>
```